Real Estate "For Sale" Sign for construction company

We need a sign that we can use to hang on a post and place on the road when we sell a property. The sign will be simple and will need to mainly feature our logo (files attached), as well as the words "For Sale", and then our phone number "(555) 617 3489". The sign will hang on a post that'll look something like the attached picture.

Target Market(s)

Home buyers

Industry/Entity Type

Real Estate

Font styles to use
Serif
Sans Serif

Colors
0054AA
0677BA
7BADD7
CADEEF
E8F1F8
0094D4
00A9DD
6FCCEA
C7EBF8
E9F6FB

Requirements
Must have
• For Sale & our phone number

```html
<!DOCTYPE html>
<html lang="en">
<head>
<meta charset="utf-8">
<title>For Sale Sign – Northgate Ridge Properties</title>
<link rel="stylesheet" href="https://fonts.googleapis.com/css2?family=Open+Sans:wght@400;700&family=Montserrat:wght@400&display=swap">
<style>
  :root {
    --canvas-bg: #eef1f4;
    --sign-bg: #ffffff;
    --brand-blue: #1a7fc4;
    --deep-navy: #14204a;
    --sky-light: #a6dcf6;
    --ridge-bright: #3fb8ec;
    --ridge-mid: #0054aa;
    --ridge-dark: #141f4a;
    --mark-blue: #0054aa;
  }
  * { margin: 0; padding: 0; box-sizing: border-box; }
  html, body {
    width: 1200px;
    height: 1200px;
    overflow: hidden;
    background: var(--canvas-bg);
  }
  .canvas {
    width: 1200px;
    height: 1200px;
    display: flex;
    align-items: center;
    justify-content: center;
  }
  .sign {
    position: relative;
    width: 830px;
    height: 1160px;
    background: var(--sign-bg);
    overflow: hidden;
    box-shadow: 0 6px 24px rgba(20, 32, 74, 0.15);
  }
  .brand {
    position: absolute;
    top: 62px;
    left: 0;
    right: 0;
    text-align: center;
    color: var(--brand-blue);
    font-family: "Montserrat", sans-serif;
    font-weight: 400;
  }
  .brand-dot {
    display: block;
    width: 104px;
    height: 104px;
    margin: 0 auto 18px;
    border-radius: 50%;
    background: var(--mark-blue);
  }
  .brand-name {
    display: block;
    font-size: 62px;
    line-height: 1;
    letter-spacing: 0.5px;
  }
  .brand-tagline {
    display: block;
    margin-top: 20px;
    font-size: 19px;
    letter-spacing: 17px;
    padding-left: 17px;
  }
  .headline {
    position: absolute;
    top: 372px;
    left: 0;
    right: 0;
    text-align: center;
    font-family: "Open Sans", sans-serif;
    font-weight: 700;
    font-size: 102px;
    line-height: 1;
    color: var(--brand-blue);
  }
  .phone {
    position: absolute;
    top: 468px;
    left: 0;
    right: 0;
    text-align: center;
    font-family: "Open Sans", sans-serif;
    font-weight: 700;
    font-size: 106px;
    line-height: 1.2;
    color: var(--deep-navy);
    letter-spacing: -1px;
  }
  .mountain-range {
    position: absolute;
    left: 0;
    right: 0;
    top: 640px;
    bottom: 0;
    background: linear-gradient(180deg, var(--sky-light) 0%, var(--ridge-bright) 30%, var(--ridge-mid) 62%, var(--ridge-dark) 100%);
  }
</style>
</head>
<body>
  <main class="canvas">
    <section class="sign">
      <header class="brand">
        <span class="brand-dot"></span>
        <span class="brand-name">Northgate Ridge</span>
        <span class="brand-tagline">PROPERTIES</span>
      </header>
      <h1 class="headline">FOR SALE</h1>
      <p class="phone">(555) 617 3489</p>
      <div class="mountain-range" role="img" aria-label="Illustration of layered blue mountain ridges, pale sky-blue peaks fading to deep navy foothills"></div>
    </section>
  </main>
</body>
</html>
```